Coffee Package Design

We need a new package design for a coffee company. Need to be a mix between modern and classic design combined together. We are open to different ideas.
We changing our product name from Café Verlona to Café Rostelli. The picture upload
shows what the product looks like. We want something completely different. The name of the company should go on the back of the package.
Updates

Hello Everyone,

Please read description, we are going with a new name and design for the product.

Café Rostelli. Café Verlona is what we are replacing with Café Rostelli, we are looking for new

look and design, please submit new designs.

There is a change in the description. Please take out Premium coffee blend and replace with Italian Roast.                                    

Industry/Entity Type

Cafe

Requirements
Must have
• You can use up to 6 colors.
Please put these items on design: Café Rostelli (this is the product name), Regular Premium Blend Coffee, 100% Arabica,
Dumbrell & Sons (name of the company), Tyler, TX on the back of the package

The file uploaded is an example of one of our products and how the package film
is sized.

```html
<!DOCTYPE html>
<html lang="en">
<head>
<meta charset="utf-8">
<title>Café Rostelli – Italian Roast Coffee Package</title>
<link rel="stylesheet" href="https://fonts.googleapis.com/css2?family=Arimo:wght@400;700&display=swap">
<style>
  :root {
    --backdrop: #ececec;
    --crimp-light: #c0844f;
    --crimp-mid: #9a5f30;
    --crimp-dark: #6e3f1c;
    --body-orange: #c4701f;
    --body-rust: #a2481c;
    --body-brown: #7a3a16;
    --text-white: #ffffff;
    --text-cream: #f3e7d6;
    --art-cream: #d9c3ae;
    --art-mocha: #9c7458;
  }

  * { margin: 0; padding: 0; box-sizing: border-box; }

  html, body {
    width: 1200px;
    height: 900px;
    overflow: hidden;
    background: var(--backdrop);
    font-family: "Arimo", Arial, sans-serif;
  }

  .canvas {
    position: relative;
    width: 1200px;
    height: 900px;
  }

  .package {
    position: absolute;
    left: 320px;
    top: 105px;
    width: 560px;
    height: 690px;
    overflow: hidden;
    box-shadow: 0 18px 30px rgba(0,0,0,0.18);
  }

  .package__crimp {
    position: absolute;
    left: 0;
    width: 100%;
    background:
      repeating-linear-gradient(to bottom,
        var(--crimp-light) 0 3px,
        var(--crimp-mid) 3px 5px,
        var(--crimp-dark) 5px 6px);
  }
  .package__crimp--top { top: 0; height: 58px; }
  .package__crimp--bottom { bottom: 0; height: 52px; }

  .package__body {
    position: absolute;
    left: 0;
    top: 58px;
    width: 100%;
    height: 580px;
    background:
      radial-gradient(ellipse 45% 22% at 62% 10%, rgba(124,138,58,0.85), transparent 75%),
      radial-gradient(ellipse 40% 25% at 80% 50%, rgba(168,70,30,0.7), transparent 80%),
      linear-gradient(160deg, var(--body-orange) 0%, var(--body-rust) 45%, var(--body-brown) 100%);
  }

  .package__facets {
    position: absolute;
    inset: 0;
    width: 100%;
    height: 100%;
  }

  .tagline {
    position: absolute;
    top: 22px;
    width: 100%;
    text-align: center;
    color: var(--text-cream);
    font-size: 13px;
    font-weight: 700;
    letter-spacing: 3px;
  }

  .product-name {
    position: absolute;
    top: 92px;
    left: 0;
    width: 100%;
    text-align: center;
    color: var(--text-white);
    font-weight: 700;
    line-height: 0.95;
  }
  .product-name__small { display: block; font-size: 58px; letter-spacing: 3px; }
  .product-name__large { display: block; font-size: 86px; letter-spacing: 2px; }

  .roast {
    position: absolute;
    top: 262px;
    width: 100%;
    text-align: center;
    color: var(--text-cream);
    font-size: 15px;
    font-weight: 700;
    letter-spacing: 4px;
  }

  .cup-illustration {
    position: absolute;
    left: 220px;
    top: 300px;
    width: 320px;
    height: 270px;
    border-radius: 28px;
    background: linear-gradient(160deg, rgba(217,195,174,0.95) 0%, var(--art-cream) 40%, var(--art-mocha) 100%);
    box-shadow: inset 0 0 0 1px rgba(255,255,255,0.25);
  }

  .origin {
    position: absolute;
    left: 62px;
    bottom: 30px;
    color: var(--text-white);
    text-align: center;
    font-weight: 700;
    line-height: 1.1;
  }
  .origin__percent { display: block; font-size: 26px; }
  .origin__bean { display: block; font-size: 16px; font-weight: 400; }
</style>
</head>
<body>
  <main class="canvas">
    <section class="package">
      <div class="package__crimp package__crimp--top"></div>

      <div class="package__body">
        <svg class="package__facets" viewBox="0 0 560 580" preserveAspectRatio="none" aria-hidden="true">
          <polygon points="0,0 140,0 30,580 0,580" fill="#ffffff" opacity="0.06"/>
          <polygon points="0,330 180,580 0,580" fill="#e09a3a" opacity="0.35"/>
          <polygon points="380,0 560,0 560,220" fill="#ffffff" opacity="0.05"/>
          <polygon points="200,580 560,380 560,580" fill="#5a2a10" opacity="0.2"/>
        </svg>

        <p class="tagline">Regular Premium Blend Coffee</p>

        <h1 class="product-name">
          <span class="product-name__small">Café</span>
          <span class="product-name__large">Rostelli</span>
        </h1>

        <p class="roast">Italian Roast</p>

        <div class="cup-illustration" role="img" aria-label="Illustration of a steaming cup of coffee on a saucer with heart-shaped steam"></div>

        <p class="origin">
          <span class="origin__percent">100%</span>
          <span class="origin__bean">Arabica</span>
        </p>
      </div>

      <div class="package__crimp package__crimp--bottom"></div>
    </section>
  </main>
</body>
</html>
```